Business Card - MosswickTreasury.com

I need a business card that has my photo. It should say: My Pemakino store can be found on at the MosswickTreasury.com. Also find my links to Pagenook, Reelhall and Clipsy. (If this can be done graphically, then that's even better)

```html
<!DOCTYPE html>
<html lang="en">
<head>
<meta charset="utf-8">
<title>Mosswick Treasury – Business Card</title>
<link rel="stylesheet" href="https://fonts.googleapis.com/css2?family=Questrial&family=Montserrat:wght@400;500;700&display=swap">
<style>
  :root {
    --stone: #8f8c87;
    --stone-light: #b4b1ac;
    --paper: #ffffff;
    --backdrop: #d6d6d6;
    --ink: #2b2b2b;
    --photo-dark: #4a4a4a;
    --photo-warm: #d9a53a;
  }
  * { margin: 0; padding: 0; box-sizing: border-box; }
  html, body { width: 1200px; height: 800px; overflow: hidden; }
  body { background: var(--backdrop); font-family: "Questrial", sans-serif; position: relative; }

  .card {
    position: absolute; width: 540px; height: 310px;
    background: var(--paper); overflow: hidden;
    box-shadow: 0 6px 18px rgba(0,0,0,.18);
  }

  /* Front */
  .card--front { left: 40px; top: 150px; }
  .front__band { position: absolute; left: 0; top: 0; width: 540px; height: 115px; background: var(--stone); }
  .front__column { position: absolute; left: 0; top: 115px; width: 60px; height: 110px; background: var(--stone); }
  .front__photo {
    position: absolute; left: 70px; top: 55px; width: 172px; height: 146px;
    border: 5px solid var(--paper); outline: 1px solid var(--stone-light);
    background: linear-gradient(160deg, var(--photo-dark) 0%, #6b6760 55%, var(--photo-warm) 100%);
  }
  .front__identity { position: absolute; left: 258px; top: 46px; color: var(--paper); }
  .front__name { font-family: "Montserrat", sans-serif; font-size: 23px; font-weight: 400; letter-spacing: .3px; }
  .front__role { font-family: "Montserrat", sans-serif; font-size: 12.5px; margin-top: 2px; }

  .front__social { position: absolute; right: 16px; top: 122px; display: flex; gap: 12px; }
  .social { display: flex; align-items: center; gap: 5px; font-family: "Montserrat", sans-serif; font-size: 11px; font-weight: 500; color: var(--ink); }
  .social__dot { width: 14px; height: 14px; border-radius: 50%; background: var(--ink); }

  .front__contacts { position: absolute; left: 258px; top: 150px; list-style: none; font-family: "Montserrat", sans-serif; font-size: 12.5px; color: var(--ink); }
  .front__contacts li { display: flex; align-items: center; gap: 7px; height: 20px; }
  .front__contacts svg { width: 12px; height: 12px; fill: none; stroke: var(--stone); stroke-width: 1.6; }
  .front__wordmark { position: absolute; left: 28px; bottom: 14px; font-size: 53px; color: var(--stone); letter-spacing: 1px; line-height: 1; }

  /* Back */
  .card--back { left: 620px; top: 380px; }
  .back__name {
    position: absolute; left: 0; right: 0; top: 88px; text-align: center;
    font-size: 52px; line-height: 1; color: var(--stone); letter-spacing: 1px;
  }
  .back__band {
    position: absolute; left: 0; top: 200px; width: 540px; height: 82px; background: var(--stone);
    color: var(--paper); font-family: "Montserrat", sans-serif; text-align: center; padding-top: 20px;
  }
  .back__line { font-size: 13px; }
  .back__url { font-size: 14px; font-weight: 700; margin-top: 3px; }
</style>
</head>
<body>

<section class="card card--front">
  <div class="front__band"></div>
  <div class="front__column"></div>
  <div class="front__photo" role="img" aria-label="Portrait photo of the store owner"></div>
  <div class="front__identity">
    <p class="front__name">Elliot Marsh</p>
    <p class="front__role">Managing Director</p>
  </div>
  <div class="front__social">
    <span class="social"><span class="social__dot"></span>Pagenook</span>
    <span class="social"><span class="social__dot"></span>Reelhall</span>
    <span class="social"><span class="social__dot"></span>Clipsy</span>
  </div>
  <ul class="front__contacts">
    <li><svg viewBox="0 0 12 12"><path d="M3 1.5 L4.6 3.5 L3.8 5 Q5 7.2 7 8.2 L8.5 7.4 L10.5 9 L9.4 10.6 Q5 10.5 1.4 3 Z"/></svg>044-987 654 321</li>
    <li><svg viewBox="0 0 12 12"><rect x="1" y="2.5" width="10" height="7"/><path d="M1 2.5 L6 6.5 L11 2.5"/></svg>hello@mosswickmail.com</li>
    <li><svg viewBox="0 0 12 12"><circle cx="6" cy="6" r="4.8"/><ellipse cx="6" cy="6" rx="2" ry="4.8"/><path d="M1.2 6 H10.8"/></svg>www.MosswickTreasury.com</li>
  </ul>
  <p class="front__wordmark">MosswickTreasury</p>
</section>

<section class="card card--back">
  <p class="back__name">Mosswick Treasury</p>
  <div class="back__band">
    <p class="back__line">My Pemakino store can be found on at the</p>
    <p class="back__url">www.MosswickTreasury.com</p>
  </div>
</section>

</body>
</html>
```